The Coral Clinic PowerPoint Design

We are looking for a new PowerPoint template design to reflect our branding and to be used for presentations at international conferences and online conferences. An example of our current template which is outdated is attached. We would like to still have a blue colour background as this represents water (but the exact background can be modified). We would like a professional, modern, and sharp feel to the templates. The template should include an Intro Slide, content slide, and closing/questions slide. The template needs to be prepared for both the standards, the 4:3 and Wide screen 16:9. Logos and branding in the attached power point can be used. Please visit our website www.thecoralclinic.example to see more about the company.

```html
<!DOCTYPE html>
<html lang="en">
<head>
<meta charset="utf-8">
<title>The Coral Clinic – Presentation Deck</title>
<link href="https://fonts.googleapis.com/css2?family=Montserrat:wght@500;700;800&family=Roboto:wght@400;700&display=swap" rel="stylesheet">
<style>
:root{
  --navy:#0d4b8e;
  --navy-dark:#0a3f7a;
  --panel:#1a62ad;
  --cyan:#1cbbe9;
  --cyan-soft:#5fcff2;
  --yellow:#f3e600;
  --white:#ffffff;
  --green:#8dc63f;
  --canvas:#f2f3f5;
  --ink:#222222;
  --brand-teal:#1fbfd8;
}
*{margin:0;padding:0;box-sizing:border-box}
html,body{width:681px;height:1200px;overflow:hidden;background:var(--canvas);font-family:Roboto,Arial,sans-serif}
.canvas{position:relative;width:681px;height:1200px;overflow:hidden}
.abs{position:absolute}

/* hero */
.hero{position:absolute;left:0;top:0;width:681px;height:284px;background:#e3e5e8}
.hero-photo{position:absolute;left:0;top:0;width:681px;height:284px;background:linear-gradient(140deg,#6f757d 0%,#9aa0a7 30%,#cfd2d6 55%,#e3e5e8 72%)}
.hero-title{position:absolute;left:40px;top:100px;font-family:Montserrat,sans-serif;font-weight:800;font-size:33px;color:var(--brand-teal);letter-spacing:-.5px}
.hero-sub{position:absolute;left:111px;top:134px;font-family:Montserrat,sans-serif;font-weight:500;font-size:35px;color:var(--ink)}

/* slides */
.s{position:absolute;width:218px;height:122px;background:var(--navy);overflow:hidden;color:var(--white)}
.photo{position:absolute}
.ttl{position:absolute;left:0;right:0;text-align:center;font-family:Montserrat,sans-serif;font-weight:700;font-size:8px;color:var(--yellow)}
.sub{position:absolute;left:0;right:0;text-align:center;font-size:2.6px;letter-spacing:1.2px;font-weight:700;color:var(--white)}
.txt{position:absolute;font-size:2.6px;line-height:1.45;color:#dfe9f5}
.hd{position:absolute;font-size:3px;font-weight:700;color:var(--white)}
.foot{position:absolute;left:0;bottom:0;width:218px;height:10px;background:var(--cyan)}
.foot.plain{background:transparent}
.badge{position:absolute;left:3px;top:2.5px;width:18px;height:5px;background:var(--green)}
.foot-t{position:absolute;left:0;right:0;top:1.5px;text-align:center;font-size:3px;font-weight:700;line-height:1.2}
.foot-t span{display:block;font-size:2.2px;letter-spacing:1.2px;font-weight:400}
.foot-b{position:absolute;right:6px;top:3px;font-size:2.8px;font-weight:700;color:var(--white)}
.dot{position:absolute;border-radius:50%}
.card{position:absolute;border-radius:3px}
.brand{font-family:Roboto,sans-serif;font-weight:700;color:var(--white)}
</style>
</head>
<body>
<div class="canvas">

  <!-- hero -->
  <section class="hero">
    <div class="hero-photo" role="img" aria-label="Photo of a cheering crowd with raised hands at sunset"></div>
    <div class="hero-title">Presentation</div>
    <div class="hero-sub">Deck</div>

    <!-- featured title slide -->
    <div class="s" style="left:318px;top:47px;width:267px;height:152px">
      <svg class="abs" style="left:0;top:0" width="267" height="152" viewBox="0 0 267 152">
        <path d="M0 110 C40 98 80 120 130 108 C180 96 220 88 267 70 L267 152 L0 152Z" fill="#fff"/>
      </svg>
      <div class="abs" style="left:24px;top:48px;font-family:Montserrat,sans-serif;font-weight:700;font-size:13px">Title Here</div>
      <div class="abs" style="left:25px;top:74px;font-size:3.2px;letter-spacing:1.6px;line-height:1.9">DR XX<br>THE CORAL CLINIC</div>
      <div class="photo" role="img" aria-label="Laptop with two sharks swimming out of the screen" style="left:130px;top:44px;width:132px;height:80px;border-radius:4px;background:linear-gradient(160deg,#9fc3d8,#3f7fa6 60%,#7c8a93)"></div>
      <div class="abs brand" style="left:40px;top:124px;font-size:6px;color:var(--navy)">The Coral Clinic</div>
      <div class="abs" style="left:230px;top:137px;width:23px;height:7px;background:var(--green)"></div>
    </div>
  </section>

  <!-- row 1 -->
  <div class="s" style="left:7px;top:289px">
    <div class="abs" style="left:70px;top:24px;font-family:Montserrat,sans-serif;font-weight:700;font-size:9px;color:var(--cyan-soft)">Add Your Title Here</div>
    <div class="abs" style="left:0;right:0;top:43px;text-align:center;font-size:2.6px;letter-spacing:1.3px;line-height:1.8">DR XX<br>THE CORAL CLINIC</div>
    <div class="photo" role="img" aria-label="Laptop with two sharks swimming out of the screen" style="left:63px;top:56px;width:96px;height:60px;border-radius:3px;background:linear-gradient(160deg,#9fc3d8,#3f7fa6 60%,#6f7c86)"></div>
    <div class="foot-b" style="bottom:3px;top:auto">The Coral Clinic</div>
  </div>

  <div class="s" style="left:231px;top:289px">
    <div class="photo" role="img" aria-label="Blue-toned photo of a spotted triggerfish" style="left:0;top:0;width:218px;height:122px;background:radial-gradient(ellipse at 52% 55%,#3f86d0 0%,#2a6fbe 35%,#1b5aa5 70%)"></div>
    <div class="abs brand" style="left:0;right:0;top:16px;text-align:center;font-size:5px">The Coral Clinic</div>
    <div class="abs" style="left:0;right:0;top:54px;text-align:center;font-family:Montserrat,sans-serif;font-weight:700;font-size:7.6px">PRESENTATION TITLE HERE</div>
    <div class="sub" style="top:66px;font-weight:400">SUB TITLE GOES HERE</div>
    <div class="abs" style="left:0;right:0;top:104px;text-align:center;font-size:2.6px;letter-spacing:1.3px;line-height:1.7">DR XX<br>THE CORAL CLINIC</div>
  </div>

  <div class="s" style="left:456px;top:289px">
    <div class="abs" style="left:0;top:0;width:21px;height:122px;background:var(--cyan)"></div>
    <div class="abs" style="left:3px;top:113px;transform:rotate(-90deg);transform-origin:0 0;font-family:Montserrat,sans-serif;font-weight:700;font-size:7px;white-space:nowrap">TABLE OF CONTENTS</div>
    <div class="photo" role="img" aria-label="Photo of a penguin swimming underwater" style="left:21px;top:0;width:87px;height:122px;background:linear-gradient(180deg,#8fd3c9,#3fa7a0 45%,#2a8893)"></div>
    <div class="txt" style="left:126px;top:20px;font-size:3.4px;line-height:2.55;color:#fff">
      i.&nbsp;&nbsp;&nbsp;&nbsp;&nbsp;&nbsp;Introduction<br>ii.&nbsp;&nbsp;&nbsp;&nbsp;&nbsp;About Us<br>iii.&nbsp;&nbsp;&nbsp;&nbsp;Welcome Message<br>iv.&nbsp;&nbsp;&nbsp;&nbsp;Company Profile<br>v.&nbsp;&nbsp;&nbsp;&nbsp;&nbsp;Team<br>vi.&nbsp;&nbsp;&nbsp;&nbsp;Team Group<br>vii.&nbsp;&nbsp;&nbsp;Portfolio<br>viii.&nbsp;&nbsp;Info graphic<br>ix.&nbsp;&nbsp;&nbsp;&nbsp;Contact Us<br>x.&nbsp;&nbsp;&nbsp;&nbsp;&nbsp;Data Chart
    </div>
    <div class="foot-b" style="bottom:3px;top:auto">The Coral Clinic</div>
  </div>

  <!-- row 2 -->
  <div class="s" style="left:7px;top:419px">
    <div class="ttl" style="top:5px">Add Your Awesome Title Here</div>
    <div class="sub" style="top:15px">HERE ADD YOUR TITLE</div>
    <div class="txt" style="left:12px;right:12px;top:26px;text-align:justify">Lorem ipsum dolor sit amet, consectetur adipiscing elit. Fusce sit amet neque sodales, faucibus ex eu, efficitur lacus. Cras imperdiet, nulla nec sagittis pulvinar, neque augue iaculis risus, ac fringilla felis urna fermentum mi. Ut vehicula vel enim sit amet vulputate. Aenean malesuada consectetur diam, ac convallis augue tincidunt eget. Nam vitae elementum ipsum. Proin vitae blandit enim. Donec congue convallis commodo. Aenean vel lacus lacus. Sed in erat ultrices dolor faucibus feugiat. Nullam cursus sollicitudin dictum. Donec a ex at enim consectetur auctor. Aliquam ut laoreet neque. Aenean molestie, libero sed suscipit tincidunt, tellus nulla dictum dui, in viverra nunc purus sodales diam. Sed ullamcorper at ante eget euismod.<br><br>Maecenas in purus at tellus tincidunt sodales eu sed nibh. Aenean justo diam, commodo vel felis ac, malesuada sodales purus. Nunc sollicitudin sed justo in eleifend. Fusce dictum ornare ligula, eu porttitor elit ullamcorper non. Aliquam erat volutpat.</div>
    <div class="foot"><div class="badge"></div><div class="foot-t">HOME OF THE REEF CARE COURSE<span>WWW.THECORALCLINIC.EXAMPLE</span></div><div class="foot-b">The Coral Clinic</div></div>
  </div>

  <div class="s" style="left:231px;top:419px">
    <div class="photo" role="img" aria-label="Photo of a clownfish beside a sea anemone" style="left:0;top:0;width:84px;height:112px;background:linear-gradient(160deg,#7a9a5a,#2f6d6a 50%,#1d4f6e)"></div>
    <div class="abs" style="left:68px;top:16px;width:100px;height:20px;background:var(--cyan);text-align:center;line-height:20px;font-family:Montserrat,sans-serif;font-weight:700;font-size:7px;color:var(--yellow)">CORAL CLINIC</div>
    <div class="txt" style="left:96px;top:49px;width:110px;font-size:3px">The Coral Clinic is dedicated to advancing the health and welfare of aquatic animals in aquariums and zoos globally. This is based upon our four pillars of care:</div>
    <div class="dot" style="left:97px;top:74px;width:5px;height:5px;background:var(--yellow)"></div>
    <div class="abs" style="left:105px;top:75px;font-size:3.2px;color:var(--yellow)">Consultation</div>
    <div class="dot" style="left:153px;top:74px;width:5px;height:5px;background:var(--yellow)"></div>
    <div class="abs" style="left:161px;top:75px;font-size:3.2px;color:var(--yellow)">Reproduction</div>
    <div class="dot" style="left:97px;top:86px;width:5px;height:5px;background:var(--yellow)"></div>
    <div class="abs" style="left:105px;top:87px;font-size:3.2px;color:var(--yellow)">Education</div>
    <div class="dot" style="left:153px;top:86px;width:5px;height:5px;background:var(--yellow)"></div>
    <div class="abs" style="left:161px;top:87px;font-size:3.2px;color:var(--yellow)">Medication</div>
    <div class="foot"><div class="badge"></div><div class="foot-t">HOME OF THE REEF CARE COURSE<span>WWW.THECORALCLINIC.EXAMPLE</span></div><div class="foot-b">The Coral Clinic</div></div>
  </div>

  <div class="s" style="left:456px;top:419px">
    <div class="abs" style="left:97px;top:0;width:18px;height:2px;background:var(--cyan)"></div>
    <div class="ttl" style="top:18px;font-size:9px">Add Your Awesome Title Here</div>
    <div class="sub" style="top:30px;font-size:3px;letter-spacing:1.6px">HERE ADD YOUR TITLE</div>
    <div class="card" style="left:16px;top:49px;width:82px;height:49px;background:var(--cyan)"></div>
    <div class="dot" style="left:21px;top:61px;width:20px;height:20px;background:var(--navy)"></div>
    <svg class="abs" style="left:27px;top:66px" width="8" height="10" viewBox="0 0 8 10"><circle cx="4" cy="3.5" r="3.2" fill="#f3e600"/><rect x="2.6" y="7" width="2.8" height="2" fill="#f3e600"/></svg>
    <div class="hd" style="left:48px;top:64px;color:#fff">Your Contents Here</div>
    <div class="txt" style="left:48px;top:70px;width:44px;font-size:2.3px">Lorem ipsum dolor sit amet, consectetur adipiscing elit, sed do eiusmod tempor incididunt.</div>
    <div class="card" style="left:120px;top:49px;width:82px;height:49px;background:var(--cyan)"></div>
    <div class="dot" style="left:125px;top:61px;width:20px;height:20px;background:var(--navy)"></div>
    <svg class="abs" style="left:130px;top:66px" width="10" height="10" viewBox="0 0 10 10"><path d="M1 5 L9 1 L6 9 L5 6Z" fill="#f3e600"/></svg>
    <div class="hd" style="left:152px;top:64px">Your Contents Here</div>
    <div class="txt" style="left:152px;top:70px;width:44px;font-size:2.3px">Lorem ipsum dolor sit amet, consectetur adipiscing elit, sed do eiusmod tempor incididunt.</div>
    <div class="foot plain"><div class="foot-t" style="font-weight:400;letter-spacing:.8px">HOME OF THE REEF CARE COURSE<span>WWW.THECORALCLINIC.EXAMPLE</span></div><div class="foot-b">The Coral Clinic</div></div>
  </div>

  <!-- row 3 -->
  <div class="s" style="left:7px;top:549px">
    <div class="ttl" style="top:14px">Add Your Awesome Title Here</div>
    <div class="sub" style="top:24px">HERE ADD YOUR TITLE</div>
    <div class="txt" style="left:12px;right:12px;top:33px;text-align:center;font-size:2.8px">Lorem ipsum dolor sit amet, consectetur adipiscing elit, sed do eiusmod tempor incididunt ut labore et dolore magna aliqua. Lorem ipsum dolor sit amet, consectetur adipiscing elit, sed do eiusmod tempor incididunt ut labore et dolore magna aliqua. Lorem ipsum dolor sit amet, consectetur adipiscing elit, sed do eiusmod tempor incididunt ut labore et dolore magna aliqua.</div>
    <svg class="abs" style="left:10px;top:68px" width="200" height="30" viewBox="0 0 200 30">
      <g fill="#1cbbe9"><circle cx="4" cy="5" r="4"/><circle cx="73" cy="5" r="4"/><circle cx="142" cy="5" r="4"/><circle cx="4" cy="23" r="4"/><circle cx="73" cy="23" r="4"/><circle cx="142" cy="23" r="4"/></g>
      <g fill="none" stroke="#fff" stroke-width="1"><path d="M2 5 L3.6 6.6 L6 3.6"/><path d="M71 5 L72.6 6.6 L75 3.6"/><path d="M140 5 L141.6 6.6 L144 3.6"/><path d="M2 23 L3.6 24.6 L6 21.6"/><path d="M71 23 L72.6 24.6 L75 21.6"/><path d="M140 23 L141.6 24.6 L144 21.6"/></g>
    </svg>
    <div class="hd" style="left:22px;top:67px">Lorem ipsum dolor</div><div class="txt" style="left:22px;top:72px;width:50px;font-size:2.2px">Lorem ipsum dolor sit amet, consectetur adipiscing elit, sed do eiusmod.</div>
    <div class="hd" style="left:91px;top:67px">Lorem ipsum dolor</div><div class="txt" style="left:91px;top:72px;width:50px;font-size:2.2px">Lorem ipsum dolor sit amet, consectetur adipiscing elit, sed do eiusmod.</div>
    <div class="hd" style="left:160px;top:67px">Lorem ipsum dolor</div><div class="txt" style="left:160px;top:72px;width:50px;font-size:2.2px">Lorem ipsum dolor sit amet, consectetur adipiscing elit, sed do eiusmod.</div>
    <div class="hd" style="left:22px;top:85px">Lorem ipsum dolor</div><div class="txt" style="left:22px;top:90px;width:50px;font-size:2.2px">Lorem ipsum dolor sit amet, consectetur adipiscing elit, sed do eiusmod.</div>
    <div class="hd" style="left:91px;top:85px">Lorem ipsum dolor</div><div class="txt" style="left:91px;top:90px;width:50px;font-size:2.2px">Lorem ipsum dolor sit amet, consectetur adipiscing elit, sed do eiusmod.</div>
    <div class="hd" style="left:160px;top:85px">Lorem ipsum dolor</div><div class="txt" style="left:160px;top:90px;width:50px;font-size:2.2px">Lorem ipsum dolor sit amet, consectetur adipiscing elit, sed do eiusmod.</div>
    <div class="foot"><div class="badge"></div><div class="foot-t">HOME OF THE REEF CARE COURSE<span>WWW.THECORALCLINIC.EXAMPLE</span></div><div class="foot-b">The Coral Clinic</div></div>
  </div>

  <div class="s" style="left:231px;top:549px">
    <div class="ttl" style="top:5px">Add Your Awesome Title Here</div>
    <div class="sub" style="top:15px">HERE ADD YOUR TITLE</div>
    <svg class="abs" style="left:22px;top:28px" width="10" height="80" viewBox="0 0 10 80"><g fill="#1cbbe9"><circle cx="5" cy="5" r="4.5"/><circle cx="5" cy="26" r="4.5"/><circle cx="5" cy="47" r="4.5"/><circle cx="5" cy="68" r="4.5"/></g><g fill="#fff" font-size="4.5" font-family="Roboto" font-weight="700" text-anchor="middle"><text x="5" y="6.6">1</text><text x="5" y="27.6">2</text><text x="5" y="48.6">3</text><text x="5" y="69.6">4</text></g></svg>
    <svg class="abs" style="left:115px;top:30px" width="10" height="80" viewBox="0 0 10 80"><g fill="#1cbbe9"><circle cx="5" cy="5" r="4.5"/><circle cx="5" cy="26" r="4.5"/><circle cx="5" cy="47" r="4.5"/><circle cx="5" cy="68" r="4.5"/></g><g fill="#fff" font-size="4.5" font-family="Roboto" font-weight="700" text-anchor="middle"><text x="5" y="6.6">5</text><text x="5" y="27.6">6</text><text x="5" y="48.6">7</text><text x="5" y="69.6">8</text></g></svg>
    <div class="hd" style="left:37px;top:25px">Contents Title</div><div class="txt" style="left:37px;top:29px;width:70px;font-size:2.2px">Lorem ipsum randomised words which don't look even slightly believable in some form.</div>
    <div class="hd" style="left:37px;top:46px">Contents Title</div><div class="txt" style="left:37px;top:50px;width:70px;font-size:2.2px">Lorem ipsum randomised words which don't look even slightly believable in some form.</div>
    <div class="hd" style="left:37px;top:67px">Contents Title</div><div class="txt" style="left:37px;top:71px;width:70px;font-size:2.2px">Lorem ipsum randomised words which don't look even slightly believable in some form.</div>
    <div class="hd" style="left:37px;top:88px">Contents Title</div><div class="txt" style="left:37px;top:92px;width:70px;font-size:2.2px">Lorem ipsum randomised words which don't look even slightly believable in some form.</div>
    <div class="hd" style="left:130px;top:25px">Contents Title</div><div class="txt" style="left:130px;top:29px;width:70px;font-size:2.2px">Lorem ipsum randomised words which don't look even slightly believable in some form.</div>
    <div class="hd" style="left:130px;top:46px">Contents Title</div><div class="txt" style="left:130px;top:50px;width:70px;font-size:2.2px">Lorem ipsum randomised words which don't look even slightly believable in some form.</div>
    <div class="hd" style="left:130px;top:67px">Contents Title</div><div class="txt" style="left:130px;top:71px;width:70px;font-size:2.2px">Lorem ipsum randomised words which don't look even slightly believable in some form.</div>
    <div class="hd" style="left:130px;top:88px">Contents Title</div><div class="txt" style="left:130px;top:92px;width:70px;font-size:2.2px">Lorem ipsum randomised words which don't look even slightly believable in some form.</div>
    <div class="foot"><div class="badge"></div><div class="foot-t">HOME OF THE REEF CARE COURSE<span>WWW.THECORALCLINIC.EXAMPLE</span></div><div class="foot-b">The Coral Clinic</div></div>
  </div>

  <div class="s" style="left:456px;top:549px">
    <svg class="abs" style="left:10px;top:9px" width="14" height="100" viewBox="0 0 14 100"><g fill="#1a62ad"><circle cx="7" cy="7" r="7"/><circle cx="7" cy="34" r="7"/><circle cx="7" cy="61" r="7"/><circle cx="7" cy="88" r="7"/></g><g fill="#f3e600"><circle cx="7" cy="7" r="3"/><circle cx="7" cy="34" r="3"/><circle cx="7" cy="61" r="3"/><circle cx="7" cy="88" r="3"/></g></svg>
    <div class="hd" style="left:32px;top:9px;color:var(--yellow);font-size:2.8px">CONSULTATION</div><div class="txt" style="left:32px;top:13px;width:178px;font-size:2.3px">The Coral Clinic provides on-site visits as well as telephone and email support to public aquariums, ornamental fish importers and breeding facilities. Our team brings many years of experience in the aquarium industry to every project and partner worldwide.</div>
    <div class="hd" style="left:32px;top:36px;color:var(--yellow);font-size:2.8px">EDUCATION</div><div class="txt" style="left:32px;top:40px;width:178px;font-size:2.3px">The Coral Clinic has developed the first online course for aquarists, launched in 2011 and now studied by students on six continents and recognised by leading zoo and aquarium bodies.</div>
    <div class="hd" style="left:32px;top:63px;color:var(--yellow);font-size:2.8px">CONFERENCES</div><div class="txt" style="left:32px;top:67px;width:178px;font-size:2.3px">The Coral Clinic, in conjunction with partner aquariums, is delighted to announce a new workshop on parasite identification and their management, held over two days in August.</div>
    <div class="hd" style="left:32px;top:90px;color:var(--yellow);font-size:2.8px">REPRODUCTION</div><div class="txt" style="left:32px;top:94px;width:178px;font-size:2.3px">Our vets have been researching elasmobranch reproduction since 2004 and have now launched a reproduction research centre to assist with the sharing of information.</div>
    <div class="foot"><div class="badge"></div><div class="foot-t">HOME OF THE REEF CARE COURSE<span>WWW.THECORALCLINIC.EXAMPLE</span></div><div class="foot-b">The Coral Clinic</div></div>
  </div>

  <!-- row 4 -->
  <div class="s" style="left:7px;top:679px">
    <div class="photo" role="img" aria-label="Deep blue underwater photo with a glowing jellyfish" style="left:0;top:0;width:218px;height:80px;background:radial-gradient(circle at 92px 30px,#7fc7f0 0%,#2a76c8 25%,#0f4f9c 60%,#0b3f85 100%)"></div>
    <div class="abs" style="left:11px;top:22px;font-family:Montserrat,sans-serif;font-weight:700;font-size:8px;line-height:1.25;color:var(--yellow)">Lorem ipsum dolor<br>sit amet elit et dolor</div>
    <div class="txt" style="left:11px;top:45px;width:80px;font-size:2.8px;color:#fff">Lorem ipsum dolor sit amet, consectetur adipiscing elit, sed do eiusmod tempor incididunt ut labore et dolore magna aliqua. Lorem ipsum dolor sit amet, consectetur adipiscing elit, sed do eiusmod.</div>
    <div class="abs" style="left:0;top:80px;width:73px;height:42px;background:#1b86d0"></div>
    <div class="abs" style="left:73px;top:80px;width:72px;height:42px;background:#1ca4e0"></div>
    <div class="abs" style="left:145px;top:80px;width:73px;height:42px;background:#1b86d0"></div>
    <div class="dot" style="left:10px;top:73px;width:14px;height:14px;background:#1b86d0"></div>
    <div class="dot" style="left:83px;top:73px;width:14px;height:14px;background:#1ca4e0"></div>
    <div class="dot" style="left:156px;top:73px;width:14px;height:14px;background:#1b86d0"></div>
    <svg class="abs" style="left:13px;top:76px" width="8" height="8" viewBox="0 0 8 8"><circle cx="4" cy="4" r="2.8" fill="none" stroke="#fff" stroke-width="1.4" stroke-dasharray="1.4 .8"/></svg>
    <svg class="abs" style="left:86px;top:76px" width="8" height="8" viewBox="0 0 8 8"><path d="M1 4 L7 1 L5 7 L4 5Z" fill="#fff"/></svg>
    <svg class="abs" style="left:159px;top:76px" width="8" height="8" viewBox="0 0 8 8"><rect x="1" y="1.5" width="6" height="4" fill="none" stroke="#fff" stroke-width=".8"/><path d="M3 7 H5" stroke="#fff" stroke-width=".8"/></svg>
    <div class="hd" style="left:8px;top:96px">Lorem ipsum dolor</div><div class="txt" style="left:8px;top:101px;width:62px;font-size:2.2px;color:#fff">Lorem ipsum dolor sit amet, consectetur adipiscing elit, sed do eiusmod tempor incididunt.</div>
    <div class="hd" style="left:80px;top:96px">Lorem ipsum dolor</div><div class="txt" style="left:80px;top:101px;width:62px;font-size:2.2px;color:#fff">Lorem ipsum dolor sit amet, consectetur adipiscing elit, sed do eiusmod tempor incididunt.</div>
    <div class="hd" style="left:152px;top:96px">Lorem ipsum dolor</div><div class="txt" style="left:152px;top:101px;width:62px;font-size:2.2px;color:#fff">Lorem ipsum dolor sit amet, consectetur adipiscing elit, sed do eiusmod tempor incididunt.</div>
  </div>

  <div class="s" style="left:231px;top:679px">
    <div class="photo" role="img" aria-label="Colourful coral reef photo with a sea turtle and tropical fish" style="left:0;top:0;width:218px;height:122px;background:linear-gradient(180deg,#2a6c8e 0%,#3a7fb0 35%,#1f5ea8 60%,#134f97 100%)"></div>
    <div class="ttl" style="top:34px">Add Your Awesome Title Here</div>
    <div class="sub" style="top:44px">HERE ADD YOUR TITLE</div>
    <div class="card" style="left:21px;top:75px;width:50px;height:40px;background:var(--cyan)"></div>
    <div class="card" style="left:80px;top:75px;width:50px;height:40px;background:var(--yellow)"></div>
    <div class="card" style="left:139px;top:75px;width:50px;height:40px;background:var(--cyan)"></div>
    <div class="hd" style="left:21px;width:50px;top:80px;text-align:center">Lorem ipsum dolor sit</div>
    <div class="txt" style="left:24px;width:44px;top:86px;text-align:center;font-size:2.1px;color:#fff">Lorem ipsum dolor sit amet, consectetur adipiscing elit, sed do eiusmod tempor incididunt ut labore et dolore magna aliqua.</div>
    <div class="hd" style="left:80px;width:50px;top:80px;text-align:center;color:var(--navy)">Lorem ipsum dolor sit</div>
    <div class="txt" style="left:83px;width:44px;top:86px;text-align:center;font-size:2.1px;color:var(--navy)">Lorem ipsum dolor sit amet, consectetur adipiscing elit, sed do eiusmod tempor incididunt ut labore et dolore magna aliqua.</div>
    <div class="hd" style="left:139px;width:50px;top:80px;text-align:center">Lorem ipsum dolor sit</div>
    <div class="txt" style="left:142px;width:44px;top:86px;text-align:center;font-size:2.1px;color:#fff">Lorem ipsum dolor sit amet, consectetur adipiscing elit, sed do eiusmod tempor incididunt ut labore et dolore magna aliqua.</div>
  </div>

  <div class="s" style="left:456px;top:679px">
    <div class="ttl" style="top:5px">Add Your Awesome Title Here</div>
    <div class="sub" style="top:15px">HERE ADD YOUR TITLE</div>
    <svg class="abs" style="left:60px;top:33px" width="100" height="66" viewBox="0 0 100 66">
      <circle cx="50" cy="33" r="31" fill="none" stroke="#1cbbe9" stroke-width=".5" stroke-dasharray="1 1"/>
      <circle cx="50" cy="33" r="25" fill="#e6f4fb"/>
      <g fill="#f3e600"><circle cx="30" cy="12" r="2"/><circle cx="70" cy="12" r="2"/><circle cx="24" cy="33" r="2"/><circle cx="76" cy="33" r="2"/><circle cx="30" cy="54" r="2"/><circle cx="70" cy="54" r="2"/></g>
    </svg>
    <div class="abs" style="left:93px;top:60px;width:34px;text-align:center;font-size:4px;font-weight:700;color:var(--navy);line-height:1.2">Add Your Awesome Title Here</div>
    <div class="card" style="left:36px;top:40px;width:36px;height:13px;background:var(--cyan)"></div><div class="txt" style="left:36px;top:45px;width:36px;text-align:center;font-size:2px;color:#fff">Composition of the board</div>
    <div class="card" style="left:31px;top:60px;width:36px;height:13px;background:var(--cyan)"></div><div class="txt" style="left:31px;top:63px;width:36px;text-align:center;font-size:2px;color:#fff">Clarity of roles &amp; responsibilities</div>
    <div class="card" style="left:34px;top:80px;width:36px;height:13px;background:var(--cyan)"></div><div class="txt" style="left:34px;top:85px;width:36px;text-align:center;font-size:2px;color:#fff">Joint vision</div>
    <div class="card" style="left:147px;top:40px;width:36px;height:13px;background:var(--cyan)"></div><div class="txt" style="left:147px;top:43px;width:36px;text-align:center;font-size:2px;color:#fff">Ability to use the strengths of all members</div>
    <div class="card" style="left:151px;top:60px;width:36px;height:13px;background:var(--cyan)"></div><div class="txt" style="left:151px;top:63px;width:36px;text-align:center;font-size:2px;color:#fff">Ability to resolve conflicts between board &amp; staff</div>
    <div class="card" style="left:146px;top:80px;width:36px;height:13px;background:var(--cyan)"></div><div class="txt" style="left:146px;top:83px;width:36px;text-align:center;font-size:2px;color:#fff">Structure &amp; organisation of the work</div>
    <div class="foot"><div class="badge"></div><div class="foot-t">HOME OF THE REEF CARE COURSE<span>WWW.THECORALCLINIC.EXAMPLE</span></div><div class="foot-b">The Coral Clinic</div></div>
  </div>

  <!-- row 5 -->
  <div class="s" style="left:7px;top:809px">
    <div class="abs" style="left:103px;top:0;width:18px;height:2px;background:var(--cyan)"></div>
    <div class="ttl" style="top:17px">Add Your Awesome Title Here</div>
    <div class="sub" style="top:27px">HERE ADD YOUR TITLE</div>
    <svg class="abs" style="left:0;top:38px" width="218" height="20" viewBox="0 0 218 20">
      <line x1="22" y1="10" x2="198" y2="10" stroke="#fff" stroke-width=".6"/>
      <g fill="#1cbbe9" stroke="#fff" stroke-width=".8"><circle cx="22" cy="10" r="2.4"/><circle cx="57" cy="10" r="2.4"/><circle cx="92" cy="10" r="2.4"/><circle cx="127" cy="10" r="2.4"/><circle cx="162" cy="10" r="2.4"/><circle cx="197" cy="10" r="2.4"/></g>
      <g stroke="#fff" stroke-width=".6"><line x1="22" y1="12.4" x2="22" y2="19"/><line x1="57" y1="12.4" x2="57" y2="19"/><line x1="92" y1="12.4" x2="92" y2="19"/><line x1="127" y1="12.4" x2="127" y2="19"/><line x1="162" y1="12.4" x2="162" y2="19"/><line x1="197" y1="12.4" x2="197" y2="19"/></g>
    </svg>
    <div class="abs" style="left:12px;top:42px;width:200px;font-size:3.2px;font-weight:700;word-spacing:0">
      <span class="abs" style="left:0">2015</span><span class="abs" style="left:35px">2016</span><span class="abs" style="left:70px">2017</span><span class="abs" style="left:105px">2018</span><span class="abs" style="left:140px">2019</span><span class="abs" style="left:175px">2020</span>
    </div>
    <div class="hd" style="left:10px;top:61px;width:24px;text-align:center;font-size:2.4px">Project name</div><div class="txt" style="left:7px;top:65px;width:30px;text-align:center;font-size:2.1px">Lorem ipsum is simply dummy text of the printing trade.</div>
    <div class="hd" style="left:45px;top:61px;width:24px;text-align:center;font-size:2.4px">Project name</div><div class="txt" style="left:42px;top:65px;width:30px;text-align:center;font-size:2.1px">Lorem ipsum is simply dummy text of the printing trade.</div>
    <div class="hd" style="left:80px;top:61px;width:24px;text-align:center;font-size:2.4px">Project name</div><div class="txt" style="left:77px;top:65px;width:30px;text-align:center;font-size:2.1px">Lorem ipsum is simply dummy text of the printing trade.</div>
    <div class="hd" style="left:115px;top:61px;width:24px;text-align:center;font-size:2.4px">Project name</div><div class="txt" style="left:112px;top:65px;width:30px;text-align:center;font-size:2.1px">Lorem ipsum is simply dummy text of the printing trade.</div>
    <div class="hd" style="left:150px;top:61px;width:24px;text-align:center;font-size:2.4px">Project name</div><div class="txt" style="left:147px;top:65px;width:30px;text-align:center;font-size:2.1px">Lorem ipsum is simply dummy text of the printing trade.</div>
    <div class="hd" style="left:185px;top:61px;width:24px;text-align:center;font-size:2.4px">Project name</div><div class="txt" style="left:182px;top:65px;width:30px;text-align:center;font-size:2.1px">Lorem ipsum is simply dummy text of the printing trade.</div>
    <div class="foot plain"><div class="foot-t" style="font-weight:400;letter-spacing:.8px">HOME OF THE REEF CARE COURSE<span>WWW.THECORALCLINIC.EXAMPLE</span></div><div class="foot-b">The Coral Clinic</div></div>
  </div>

  <div class="s" style="left:231px;top:809px">
    <div class="ttl" style="top:5px">Add Your Awesome Title Here</div>
    <div class="sub" style="top:15px">HERE ADD YOUR TITLE</div>
    <div class="abs" style="left:14px;top:33px;width:40px;height:13px;background:var(--panel);font-size:2.6px;font-weight:700;line-height:13px;text-align:center">Business valuation</div>
    <div class="abs" style="left:55px;top:33px;width:148px;height:13px;background:#fff"></div><div class="txt" style="left:57px;top:34px;width:144px;font-size:2.1px;color:#333">Lorem ipsum dolor sit amet, consectetur adipiscing elit, sed do eiusmod tempor incididunt ut labore et dolore magna aliqua. Ut enim ad minim veniam, quis nostrud exercitation ullamco laboris.</div>
    <div class="abs" style="left:14px;top:49px;width:40px;height:13px;background:var(--panel);font-size:2.6px;font-weight:700;line-height:13px;text-align:center">Business valuation</div>
    <div class="abs" style="left:55px;top:49px;width:148px;height:13px;background:#fff"></div><div class="txt" style="left:57px;top:50px;width:144px;font-size:2.1px;color:#333">Lorem ipsum dolor sit amet, consectetur adipiscing elit, sed do eiusmod tempor incididunt ut labore et dolore magna aliqua. Ut enim ad minim veniam, quis nostrud exercitation ullamco laboris.</div>
    <div class="abs" style="left:14px;top:65px;width:40px;height:13px;background:var(--panel);font-size:2.6px;font-weight:700;line-height:13px;text-align:center">Business valuation</div>
    <div class="abs" style="left:55px;top:65px;width:148px;height:13px;background:#fff"></div><div class="txt" style="left:57px;top:66px;width:144px;font-size:2.1px;color:#333">Lorem ipsum dolor sit amet, consectetur adipiscing elit, sed do eiusmod tempor incididunt ut labore et dolore magna aliqua. Ut enim ad minim veniam, quis nostrud exercitation ullamco laboris.</div>
    <div class="abs" style="left:14px;top:81px;width:40px;height:13px;background:var(--panel);font-size:2.6px;font-weight:700;line-height:13px;text-align:center">Business valuation</div>
    <div class="abs" style="left:55px;top:81px;width:148px;height:13px;background:#fff"></div><div class="txt" style="left:57px;top:82px;width:144px;font-size:2.1px;color:#333">Lorem ipsum dolor sit amet, consectetur adipiscing elit, sed do eiusmod tempor incididunt ut labore et dolore magna aliqua. Ut enim ad minim veniam, quis nostrud exercitation ullamco laboris.</div>
    <div class="foot"><div class="badge"></div><div class="foot-t">HOME OF THE REEF CARE COURSE<span>WWW.THECORALCLINIC.EXAMPLE</span></div><div class="foot-b">The Coral Clinic</div></div>
  </div>

  <div class="s" style="left:456px;top:809px">
    <div class="ttl" style="top:5px">Add Your Awesome Title Here</div>
    <div class="sub" style="top:15px">HERE ADD YOUR TITLE</div>
    <svg class="abs" style="left:77px;top:38px" width="64" height="56" viewBox="0 0 64 56">
      <path d="M8 16 L8 10 L40 10 L40 4 L52 14 L40 24 L40 18 L16 18 L16 16Z" fill="#1ca4e0"/>
      <path d="M48 16 L56 16 L56 42 L62 42 L52 54 L42 42 L48 42Z" fill="#1b86d0"/>
      <path d="M56 46 L56 48 L24 48 L24 54 L12 44 L24 34 L24 40 L48 40 L48 46Z" fill="#1ca4e0"/>
      <path d="M16 40 L8 40 L8 14 L2 14 L12 2 L22 14 L16 14Z" fill="#1b86d0"/>
    </svg>
    <div class="abs" style="left:100px;top:50px;font-size:2.2px;color:#fff">Your Text Here</div>
    <div class="abs" style="left:92px;top:87px;font-size:2.2px;color:#fff">Your Text Here</div>
    <div class="hd" style="left:53px;top:40px">Step 01</div><div class="txt" style="left:20px;top:45px;font-size:2.3px;color:#fff">Lorem ipsum dolor consectetur dolor</div>
    <div class="hd" style="left:141px;top:40px">Step 01</div><div class="txt" style="left:143px;top:45px;font-size:2.3px;color:#fff">Lorem ipsum dolor consectetur dolor</div>
    <div class="hd" style="left:53px;top:90px">Step 03</div><div class="txt" style="left:20px;top:95px;font-size:2.3px;color:#fff">Lorem ipsum dolor consectetur dolor</div>
    <div class="hd" style="left:141px;top:90px">Step 04</div><div class="txt" style="left:143px;top:95px;font-size:2.3px;color:#fff">Lorem ipsum dolor consectetur dolor</div>
    <div class="foot"><div class="badge"></div><div class="foot-t">HOME OF THE REEF CARE COURSE<span>WWW.THECORALCLINIC.EXAMPLE</span></div><div class="foot-b">The Coral Clinic</div></div>
  </div>

  <!-- row 6 -->
  <div class="s" style="left:7px;top:939px">
    <div class="ttl" style="top:18px;font-size:9px">Your awesome text here</div>
    <div class="txt" style="left:40px;right:40px;top:32px;text-align:center;font-size:2.5px;color:#fff">Lorem ipsum is simply dummy text of the printing and typesetting industry. It has been the standard dummy text ever since the 1500s, when an unknown printer took a galley of type and scrambled it to make a type specimen book.</div>
    <svg class="abs" style="left:48px;top:53px" width="126" height="32" viewBox="0 0 126 32">
      <g fill="none" stroke-width="2.6">
        <circle cx="16" cy="16" r="13" stroke="#0a3f7a"/><circle cx="16" cy="16" r="13" stroke="#1cbbe9" stroke-dasharray="40.8 81.7" transform="rotate(-90 16 16)"/>
        <circle cx="62" cy="16" r="13" stroke="#0a3f7a"/><circle cx="62" cy="16" r="13" stroke="#1cbbe9" stroke-dasharray="61.3 81.7" transform="rotate(-90 62 16)"/>
        <circle cx="108" cy="16" r="13" stroke="#0a3f7a"/><circle cx="108" cy="16" r="13" stroke="#1cbbe9" stroke-dasharray="32.7 81.7" transform="rotate(-90 108 16)"/>
      </g>
      <g fill="#fff" font-family="Montserrat" font-weight="700" font-size="6.5" text-anchor="middle"><text x="16" y="18.5">50%</text><text x="62" y="18.5">75%</text><text x="108" y="18.5">40%</text></g>
    </svg>
    <div class="txt" style="left:48px;top:88px;width:32px;text-align:center;font-size:2.3px;color:#fff">Lorem ipsum dolor amet amet consectetur dolor</div>
    <div class="txt" style="left:94px;top:88px;width:32px;text-align:center;font-size:2.3px;color:#fff">Lorem ipsum dolor amet amet consectetur dolor</div>
    <div class="txt" style="left:140px;top:88px;width:32px;text-align:center;font-size:2.3px;color:#fff">Lorem ipsum dolor amet amet consectetur dolor</div>
    <div class="foot"><div class="badge"></div><div class="foot-t">HOME OF THE REEF CARE COURSE<span>WWW.THECORALCLINIC.EXAMPLE</span></div><div class="foot-b">The Coral Clinic</div></div>
  </div>

  <div class="s" style="left:231px;top:939px">
    <div class="abs" style="left:142px;top:0;width:76px;height:122px;background:var(--panel)"></div>
    <svg class="abs" style="left:8px;top:26px" width="130" height="80" viewBox="0 0 130 80">
      <g stroke="#4f85bf" stroke-width=".35"><line x1="8" y1="2" x2="126" y2="2"/><line x1="8" y1="14" x2="126" y2="14"/><line x1="8" y1="26" x2="126" y2="26"/><line x1="8" y1="38" x2="126" y2="38"/><line x1="8" y1="50" x2="126" y2="50"/><line x1="8" y1="62" x2="126" y2="62"/></g>
      <g fill="#1ca4e0"><rect x="14" y="26" width="5" height="36"/><rect x="44" y="22" width="5" height="40"/><rect x="74" y="24" width="5" height="38"/><rect x="104" y="14" width="5" height="48"/></g>
      <g fill="#7fb0d8"><rect x="20" y="42" width="5" height="20"/><rect x="50" y="34" width="5" height="28"/><rect x="80" y="46" width="5" height="16"/><rect x="110" y="30" width="5" height="32"/></g>
      <g fill="#f3e600"><rect x="26" y="46" width="5" height="16"/><rect x="56" y="48" width="5" height="14"/><rect x="86" y="36" width="5" height="26"/><rect x="116" y="6" width="5" height="56"/></g>
      <g fill="#cfe0f0" font-family="Roboto" font-size="3.2" text-anchor="middle"><text x="22" y="69">Category 1</text><text x="52" y="69">Category 2</text><text x="82" y="69">Category 3</text><text x="112" y="69">Category 4</text></g>
      <g font-family="Roboto" font-size="2" fill="#cfe0f0"><rect x="45" y="75" width="2" height="2" fill="#1ca4e0"/><text x="48" y="77">Series 1</text><rect x="57" y="75" width="2" height="2" fill="#7fb0d8"/><text x="60" y="77">Series 2</text><rect x="69" y="75" width="2" height="2" fill="#f3e600"/><text x="72" y="77">Series 3</text></g>
    </svg>
    <div class="dot" style="left:151px;top:31px;width:15px;height:15px;background:var(--yellow)"></div><div class="abs" style="left:151px;top:36px;width:15px;text-align:center;font-size:3.4px;font-weight:700;color:var(--navy)">01</div>
    <div class="hd" style="left:169px;top:31px">Project name</div><div class="txt" style="left:169px;top:35px;width:44px;font-size:2.1px">Lorem ipsum dolor sit amet, nec an dictas quidam. Has commune accommodare no.</div>
    <div class="dot" style="left:151px;top:54px;width:15px;height:15px;background:var(--yellow)"></div><div class="abs" style="left:151px;top:59px;width:15px;text-align:center;font-size:3.4px;font-weight:700;color:var(--navy)">02</div>
    <div class="hd" style="left:169px;top:54px">Project name</div><div class="txt" style="left:169px;top:58px;width:44px;font-size:2.1px">Lorem ipsum dolor sit amet, nec an dictas quidam. Has commune accommodare no.</div>
    <div class="dot" style="left:151px;top:77px;width:15px;height:15px;background:var(--yellow)"></div><div class="abs" style="left:151px;top:82px;width:15px;text-align:center;font-size:3.4px;font-weight:700;color:var(--navy)">03</div>
    <div class="hd" style="left:169px;top:77px">Project name</div><div class="txt" style="left:169px;top:81px;width:44px;font-size:2.1px">Lorem ipsum dolor sit amet, nec an dictas quidam. Has commune accommodare no.</div>
    <div class="foot-b" style="bottom:3px;top:auto;right:36px">The Coral Clinic</div>
  </div>

  <div class="s" style="left:456px;top:939px">
    <div class="ttl" style="top:5px">Add Your Awesome Title Here</div>
    <div class="sub" style="top:15px">HERE ADD YOUR TITLE</div>
    <div class="abs" style="left:19px;top:35px;width:180px;height:9px;background:#1ca4e0"></div>
    <div class="abs" style="left:109px;top:35px;width:45px;height:9px;background:#fff"></div>
    <div class="abs" style="left:19px;top:38px;width:45px;text-align:center;font-size:2.8px;font-weight:700">ADD YOUR TITLE</div>
    <div class="abs" style="left:64px;top:38px;width:45px;text-align:center;font-size:2.8px;font-weight:700">ADD YOUR TITLE</div>
    <div class="abs brand" style="left:109px;top:38px;width:45px;text-align:center;font-size:2.8px;color:var(--navy)">The Coral Clinic</div>
    <div class="abs" style="left:154px;top:38px;width:45px;text-align:center;font-size:2.8px;font-weight:700">ADD YOUR TITLE</div>
    <div class="abs" style="left:19px;top:44px;width:90px;height:56px;background:#eef2f6"></div>
    <div class="abs" style="left:154px;top:44px;width:45px;height:56px;background:#eef2f6"></div>
    <div class="abs" style="left:109px;top:44px;width:45px;height:56px;background:#1ca4e0"></div>
    <div class="abs" style="left:64px;top:44px;width:.4px;height:56px;background:#c9d3de"></div>
    <div class="abs" style="left:19px;top:72px;width:180px;height:.4px;background:#c9d3de"></div>
    <div class="hd" style="left:24px;top:48px;color:#333;font-size:2.5px">Project name</div><div class="txt" style="left:24px;top:52px;width:36px;font-size:2px;color:#666">Lorem ipsum is simply dummy text an unknown printer took a galley.</div>
    <div class="hd" style="left:69px;top:48px;color:#333;font-size:2.5px">Project name</div><div class="txt" style="left:69px;top:52px;width:36px;font-size:2px;color:#666">Lorem ipsum is simply dummy text an unknown printer took a galley.</div>
    <div class="hd" style="left:114px;top:48px;font-size:2.5px">Project name</div><div class="txt" style="left:114px;top:52px;width:36px;font-size:2px;color:#fff">Lorem ipsum is simply dummy text an unknown printer took a galley.</div>
    <div class="hd" style="left:159px;top:48px;color:#333;font-size:2.5px">Project name</div><div class="txt" style="left:159px;top:52px;width:36px;font-size:2px;color:#666">Lorem ipsum is simply dummy text an unknown printer took a galley.</div>
    <div class="hd" style="left:24px;top:76px;color:#333;font-size:2.5px">Project name</div><div class="txt" style="left:24px;top:80px;width:36px;font-size:2px;color:#666">Lorem ipsum is simply dummy text an unknown printer took a galley.</div>
    <div class="hd" style="left:69px;top:76px;color:#333;font-size:2.5px">Project name</div><div class="txt" style="left:69px;top:80px;width:36px;font-size:2px;color:#666">Lorem ipsum is simply dummy text an unknown printer took a galley.</div>
    <div class="hd" style="left:114px;top:76px;font-size:2.5px">Project name</div><div class="txt" style="left:114px;top:80px;width:36px;font-size:2px;color:#fff">Lorem ipsum is simply dummy text an unknown printer took a galley.</div>
    <div class="hd" style="left:159px;top:76px;color:#333;font-size:2.5px">Project name</div><div class="txt" style="left:159px;top:80px;width:36px;font-size:2px;color:#666">Lorem ipsum is simply dummy text an unknown printer took a galley.</div>
    <div class="foot"><div class="badge"></div><div class="foot-t">HOME OF THE REEF CARE COURSE<span>WWW.THECORALCLINIC.EXAMPLE</span></div><div class="foot-b">The Coral Clinic</div></div>
  </div>

  <!-- row 7 -->
  <div class="s" style="left:122px;top:1069px">
    <div class="abs" style="left:100px;top:0;width:18px;height:2px;background:var(--cyan)"></div>
    <div class="ttl" style="top:5px">Add Your Awesome Title Here</div>
    <div class="sub" style="top:15px">HERE ADD YOUR TITLE</div>
    <div class="abs" style="left:56px;top:29px;width:51px;height:84px;background:#7fa6cc"></div>
    <div class="abs" style="left:162px;top:29px;width:51px;height:84px;background:#7fa6cc"></div>
    <div class="photo dot" role="img" aria-label="Team member portrait" style="left:9px;top:34px;width:26px;height:26px;background:#5b7085"></div>
    <div class="photo dot" role="img" aria-label="Team member portrait" style="left:61px;top:34px;width:26px;height:26px;background:#5b7085"></div>
    <div class="photo dot" role="img" aria-label="Team member portrait" style="left:115px;top:34px;width:26px;height:26px;background:#5b7085"></div>
    <div class="photo dot" role="img" aria-label="Team member portrait" style="left:167px;top:34px;width:26px;height:26px;background:#5b7085"></div>
    <div class="hd" style="left:10px;top:67px">Your Name</div><div class="txt" style="left:10px;top:71px;font-size:2.8px">Founder</div><div class="txt" style="left:10px;top:76px;width:42px;font-size:2px">Lorem ipsum dolor sit amet, consectetur adipiscing elit. Donec mauris lorem, vestibulum ac rutrum id.</div>
    <div class="hd" style="left:61px;top:67px">Your Name</div><div class="txt" style="left:61px;top:71px;font-size:2.8px;color:#fff">Global Account Executive</div><div class="txt" style="left:61px;top:76px;width:42px;font-size:2px;color:#fff">Lorem ipsum dolor sit amet, consectetur adipiscing elit. Donec mauris lorem, vestibulum ac rutrum id.</div>
    <div class="hd" style="left:115px;top:67px">Your Name</div><div class="txt" style="left:115px;top:71px;font-size:2.8px">Founder</div><div class="txt" style="left:115px;top:76px;width:42px;font-size:2px">Lorem ipsum dolor sit amet, consectetur adipiscing elit. Donec mauris lorem, vestibulum ac rutrum id.</div>
    <div class="hd" style="left:167px;top:67px">Your Name</div><div class="txt" style="left:167px;top:71px;font-size:2.8px;color:#fff">Global Account Executive</div><div class="txt" style="left:167px;top:76px;width:42px;font-size:2px;color:#fff">Lorem ipsum dolor sit amet, consectetur adipiscing elit. Donec mauris lorem, vestibulum ac rutrum id.</div>
    <div class="abs" style="left:9px;top:112px;width:46px;height:1px;background:var(--cyan)"></div>
    <div class="abs" style="left:56px;top:112px;width:51px;height:1px;background:var(--yellow)"></div>
    <div class="abs" style="left:113px;top:112px;width:46px;height:1px;background:var(--cyan)"></div>
    <div class="abs" style="left:162px;top:112px;width:51px;height:1px;background:var(--yellow)"></div>
    <div class="foot plain" style="bottom:-1px"><div class="foot-t" style="font-weight:400;letter-spacing:.8px">HOME OF THE REEF CARE COURSE<span>WWW.THECORALCLINIC.EXAMPLE</span></div><div class="foot-b">The Coral Clinic</div></div>
  </div>

  <div class="s" style="left:346px;top:1069px">
    <svg class="abs" style="left:46px;top:24px" width="130" height="12" viewBox="0 0 130 12">
      <g fill="none" stroke="#1cbbe9" stroke-width=".8"><circle cx="4" cy="4" r="3"/><path d="M1 4 H7 M4 1 C2 3 2 5 4 7 C6 5 6 3 4 1"/></g>
      <path d="M36 1 C34 1 33 2.5 33 3.5 C33 5 36 8 36 8 C36 8 39 5 39 3.5 C39 2.5 38 1 36 1Z" fill="#1cbbe9"/>
      <path d="M68 1 L70 1 L71 3 L70 4 C70.5 5 71.5 6 72.5 6.5 L73.5 5.5 L75.5 6.5 L75.5 8 C72 8.5 67.5 4 68 1Z" fill="#1cbbe9"/>
      <rect x="102" y="1.5" width="7" height="5" fill="#1cbbe9"/><path d="M102 1.5 L105.5 4.5 L109 1.5" fill="none" stroke="#0d4b8e" stroke-width=".6"/>
    </svg>
    <div class="abs" style="left:46px;top:33px;font-size:2.4px">www.website.example</div>
    <div class="abs" style="left:76px;top:32px;font-size:2.4px;line-height:1.2">Here to write your<br>Company adress</div>
    <div class="abs" style="left:110px;top:33px;font-size:2.4px">(555) 010-0505</div>
    <div class="abs" style="left:144px;top:33px;font-size:2.4px">info@website.example</div>
    <div class="abs" style="left:35px;top:41px;width:150px;height:.5px;background:var(--yellow)"></div>
    <div class="abs" style="left:0;right:0;top:62px;text-align:center;font-family:Montserrat,sans-serif;font-weight:700;font-size:15px;letter-spacing:.5px;color:var(--cyan-soft)">Questions?</div>
    <div class="foot-b" style="bottom:3px;top:auto">The Coral Clinic</div>
  </div>

</div>
</body>
</html>
```